v eLiquid Label

We are an electronic cigarette eLiquid manufacturer with an outdated label design which needs to be updated and become more modern. All information listed on the label cannot be changed or removed.

There are 4 colour coding on the labels that cannot change.
0mg is white
12mg is yellow
18mg is blue
24mg is red

We prefer a blue type background however are not committed to it with the proper design however if a new colour is chosen it must compliment the colour band for each colour coding

The "dots" on the front of the bottle need to be larger.

The "V" on the front needs to be in this font however we can accept slight changes to it for effect.

Issues we are facing:
The 0mg and the 18mg look too close in colour and need to be completely different in colouring.

The background colouring is too dark and you cannot see the 50/50 in the watermark.

Reason: We have not received a design which is suitable to our needs. We have see a few close ones however not exact. Thanks

Reason: I was forced to go out of country for a family emergency and to be fair I am extending the deadline

```html
<!DOCTYPE html>
<html lang="en">
<head>
<meta charset="utf-8">
<title>Nova E-Liquid Label – Sweet Tobacco 24 mg/ml</title>
<link rel="stylesheet" href="https://fonts.googleapis.com/css2?family=Arimo:wght@400;700&display=swap">
<style>
  :root {
    --band-red: #e3100f;
    --deep-red: #5a0a0a;
    --ink: #111111;
    --label-blue: #a9dcf3;
    --label-blue-light: #cdeefb;
    --smoke-blue: #7fb6d3;
    --paper: #ffffff;
  }
  * { box-sizing: border-box; margin: 0; padding: 0; }
  html, body { width: 1200px; height: 400px; overflow: hidden; background: #ffffff; }
  body { font-family: "Arimo", Arial, sans-serif; color: var(--ink); }

  .label {
    position: relative;
    width: 1200px;
    height: 400px;
    overflow: hidden;
    background: linear-gradient(180deg, var(--label-blue-light) 0%, var(--label-blue) 55%, var(--label-blue-light) 100%);
  }

  .smoke-backdrop {
    position: absolute;
    inset: 27px 0 23px 0;
    background:
      radial-gradient(ellipse 260px 80px at 140px 320px, rgba(127,182,211,.55), transparent 70%),
      radial-gradient(ellipse 300px 70px at 1040px 330px, rgba(127,182,211,.5), transparent 70%),
      radial-gradient(ellipse 180px 60px at 600px 150px, rgba(127,182,211,.35), transparent 70%);
  }

  .strength-band, .danger-band {
    position: absolute;
    left: 0;
    width: 1200px;
    background: var(--band-red);
    display: flex;
    justify-content: space-around;
    align-items: center;
    font-weight: 700;
    white-space: nowrap;
  }
  .strength-band { top: 0; height: 27px; font-size: 16px; }
  .danger-band { bottom: 0; height: 23px; font-size: 15px; }

  .ratio-watermark {
    position: absolute;
    left: 470px;
    top: 44px;
    width: 300px;
    font-weight: 700;
    font-size: 96px;
    line-height: 96px;
    color: rgba(255,255,255,.35);
    letter-spacing: 2px;
  }

  .hazard-icon { position: absolute; left: 20px; top: 40px; }

  .panel-fr {
    position: absolute;
    left: 70px;
    top: 38px;
    width: 338px;
    text-align: right;
    font-size: 15px;
    line-height: 19px;
  }
  .panel-en {
    position: absolute;
    left: 837px;
    top: 38px;
    width: 340px;
    font-size: 15px;
    line-height: 19px;
  }
  .heading { font-weight: 700; }
  .block { margin-bottom: 14px; }
  .strong-note { font-weight: 700; font-size: 15.5px; }
  .maker { font-size: 14.5px; line-height: 18px; color: #222; }

  .batch-box {
    display: flex;
    background: var(--paper);
    height: 34px;
    align-items: center;
    font-size: 14.5px;
    padding-left: 6px;
    margin: 4px 0 14px;
  }
  .batch-box span { width: 160px; }

  .brand-name {
    position: absolute;
    left: 440px;
    top: 70px;
    width: 320px;
    text-align: center;
    font-weight: 700;
    font-size: 96px;
    line-height: 1;
    color: var(--ink);
  }
  .strength-badge {
    position: absolute;
    left: 645px;
    top: 205px;
    width: 64px;
    height: 64px;
    border-radius: 50%;
    background: var(--band-red);
    border: 3px solid var(--paper);
    color: var(--paper);
    font-weight: 700;
    font-size: 34px;
    display: flex;
    align-items: center;
    justify-content: center;
  }
  .product-type {
    position: absolute;
    left: 480px;
    top: 266px;
    width: 240px;
    text-align: center;
    font-size: 22px;
  }
  .flavour-pill {
    position: absolute;
    left: 462px;
    top: 300px;
    width: 276px;
    height: 36px;
    border-radius: 14px;
    background: var(--band-red);
    border: 3px solid var(--paper);
    box-shadow: 0 0 0 2px var(--deep-red);
    color: var(--paper);
    font-size: 24px;
    display: flex;
    align-items: center;
    justify-content: center;
  }
  .volume {
    position: absolute;
    left: 520px;
    top: 350px;
    width: 160px;
    text-align: center;
    font-size: 16px;
  }

  .dot-cluster {
    position: absolute;
    width: 70px;
    height: 66px;
    background: linear-gradient(135deg, var(--deep-red), #9a1212);
    opacity: .85;
  }
  .dot-cluster.top-left { left: 442px; top: 40px; }
  .dot-cluster.top-right { left: 714px; top: 34px; }
  .dot-cluster.bottom-left { left: 434px; top: 312px; }
  .dot-cluster.bottom-right { left: 714px; top: 312px; }
</style>
</head>
<body>
<main class="label">
  <div class="smoke-backdrop" role="img" aria-label="Soft blue smoke wisps drifting across the label background"></div>

  <div class="strength-band">
    <span>24 mg/ml</span><span>24 mg/ml</span><span>24 mg/ml</span><span>24 mg/ml</span><span>24 mg/ml</span><span>24 mg/ml</span><span>24 mg/ml</span><span>24 mg/ml</span><span>24 mg/ml</span><span>24 mg/ml</span><span>24 mg/ml</span>
  </div>

  <div class="ratio-watermark">50/50<br>50/50<br>50/50</div>

  <svg class="hazard-icon" width="56" height="50" viewBox="0 0 56 50" aria-label="Hazard warning">
    <polygon points="28,3 53,47 3,47" fill="#ffffff" stroke="#111111" stroke-width="4" stroke-linejoin="round"/>
    <rect x="25" y="17" width="6" height="17" fill="#111111"/>
    <rect x="25" y="37" width="6" height="6" fill="#111111"/>
  </svg>

  <section class="panel-fr" lang="fr">
    <div class="block">
      <p class="heading">CONTENIR NOCIF</p>
      <p>Ne pas avaler.</p>
      <p>Ne pas mettre dans les yeux ou sur la peau ou les vetements.</p>
      <p>Tenir hors de portee des enfants et des animaux.</p>
    </div>
    <div class="block">
      <p><span class="heading">INGREDIENTS:</span> Propylene Glycol, Glycerine, Alcool de Qualite Alimentaire, Aromes Naturel et Artificiels.</p>
    </div>
    <div class="block">
      <p class="strong-note">En cas d’ingestion consulter centre antipoison ou un medecin immediatement. Peux contenir de noix.</p>
    </div>
    <p class="maker">Produit et emballe exclusivement pour:<br>5521907 Canada Inc., Elmridge ON<br>K0B 3M0</p>
  </section>

  <div class="dot-cluster top-left" role="img" aria-label="Cluster of red and dark red square dots"></div>
  <div class="dot-cluster top-right" role="img" aria-label="Cluster of red and dark red square dots"></div>
  <div class="dot-cluster bottom-left" role="img" aria-label="Cluster of red and dark red square dots"></div>
  <div class="dot-cluster bottom-right" role="img" aria-label="Cluster of red and dark red square dots"></div>

  <h1 class="brand-name">NOVA</h1>
  <div class="strength-badge">24</div>
  <p class="product-type">E-LIQUID</p>
  <p class="flavour-pill">SWEET TOBACCO</p>
  <p class="volume">vol. 30ml</p>

  <section class="panel-en">
    <div class="block">
      <p class="heading">WARNING CONTENTS HARMFUL!</p>
      <p>Do not swallow.</p>
      <p>Do not get in eyes or on skin or clothing.</p>
      <p>Keep out of reach of children and pets.</p>
    </div>
    <div class="block">
      <p><span class="heading">INGREDIENTS:</span> Propylene Glycol, Vegetable GLycerin, Nicotine (1.2%), Food Grade Alcohol, Natural and Artificial Flavours.</p>
    </div>
    <p class="strong-note">If swallowed consult poison control center or a doctor immediately. May contain nuts.</p>
    <div class="batch-box"><span>BATCH:</span><span>EXPIRES:</span></div>
    <p class="maker">Produced and Packaged exclusively for:<br>5521907 Canada Inc., Elmridge ON,<br>K0B 3M0</p>
  </section>

  <div class="danger-band">
    <span>DANGER&nbsp; POISON</span><span>DANGER&nbsp; POISON</span><span>DANGER&nbsp; POISON</span><span>DANGER&nbsp; POISON</span><span>DANGER&nbsp; POISON</span><span>DANGER&nbsp; POISON</span><span>DANGER&nbsp; POISON</span><span>DANGER&nbsp; POISON</span>
  </div>
</main>
</body>
</html>
```